Aviation security consulting company needs a website

We need a website design for Brisk Holloway, and aviation security consulting company. Brisk Holloway (www.briskholloway.example) is an aviation security consulting company that works with government and industry stakeholders in over 60 countries on aviation security strategy, governance, and oversight at the regulatory and operational level.
Brisk Holloway is strongly internationally focused.
The website required should be simple, corporate, serious, and communicate professionalism, reliability and honesty. We are trying to give the company a feeling of being well established.
The attached files include the company logo, along with examples of company web page styles that we like.
The Brisk Holloway website need only be around five pages long (landing page, who we are, our services, our clients, contact), though don't feel limited to only five pages.
The existing website (www.briskholloway.example) was rushed and put together using Wix. We don't love the existing website as it looks too amateur, so don't use it as a template.
There is no requirement for any online sales tools to be included in the site. The site is purely informational, with the option of people making contact via email.

```html
<!DOCTYPE html>
<html lang="en">
<head>
<meta charset="utf-8">
<title>Brisk Holloway — Aviation Security Consulting</title>
<link rel="stylesheet" href="https://fonts.googleapis.com/css2?family=Montserrat:wght@300;400;500;600;700&display=swap">
<style>
  :root{
    --navy:#14305f;
    --nav:#1b3a6b;
    --blue:#1378c8;
    --heading:#1a5a96;
    --gold:#f2c318;
    --orange:#f5a213;
    --text:#585858;
    --muted:#9a9a9a;
    --logo-grey:#c4c4c4;
    --panel:#f6f6f6;
    --white:#ffffff;
    --rule:#dcdcdc;
  }
  *{box-sizing:border-box;margin:0;padding:0}
  html,body{width:1200px;height:1200px;overflow:hidden;background:var(--white)}
  body{position:relative;font-family:"Montserrat",Arial,sans-serif;color:var(--text)}

  .brand{position:absolute;left:130px;top:38px;display:flex;align-items:center;gap:10px}
  .brand-mark{width:53px;height:53px;background:var(--navy)}
  .brand-name{font-size:27px;font-weight:700;color:var(--navy);line-height:1;letter-spacing:-0.5px}
  .brand-tag{font-size:11px;font-weight:400;color:var(--navy);letter-spacing:2.2px;margin-top:2px}

  .main-nav{position:absolute;right:130px;top:69px;display:flex;gap:22px}
  .main-nav a{font-size:12.4px;font-weight:500;color:var(--nav);text-decoration:none;letter-spacing:.3px}

  .hero-band{position:absolute;left:0;top:159px;width:1200px;height:137px;
    background:linear-gradient(180deg,#3b5b93 0%,#2f4f86 55%,#3a5a8a 100%)}
  .hero-title{position:absolute;left:628px;top:203px;font-size:28.5px;font-weight:500;color:var(--white);line-height:34px}

  .hero-frame{position:absolute;left:132px;top:126px;width:454px;height:372px;background:var(--white);
    padding:5px;box-shadow:0 2px 8px rgba(0,0,0,.22)}
  .hero-photo{width:100%;height:100%;background:linear-gradient(180deg,#bcd6ea 0%,#b9b7ad 30%,#c9c9c4 60%,#b8b7b2 100%)}

  .slider-dots{position:absolute;left:310px;top:516px;display:flex;gap:7.5px}
  .slider-dots span{width:13px;height:13px;border-radius:50%;background:#c8c8c8}
  .slider-dots span.active{background:var(--orange)}

  .hero-copy{position:absolute;left:631px;top:326px;width:440px;font-size:13px;font-weight:400;line-height:18.8px}
  .hero-copy p+p{margin-top:18.8px}
  .btn-read{position:absolute;left:632px;top:495px;width:119px;height:27px;background:var(--blue);color:var(--white);
    font-size:13px;font-weight:500;display:flex;align-items:center;justify-content:center;letter-spacing:.3px;text-decoration:none}

  .practice{position:absolute;left:0;top:588px;width:1200px;height:388px;background:var(--panel)}
  .practice h2{position:absolute;left:0;right:0;top:44px;text-align:center;font-size:27px;font-weight:500;color:var(--heading)}
  .practice .underline{position:absolute;left:516px;top:84px;width:123px;height:2px;background:var(--gold)}
  .practice .intro{position:absolute;left:190px;top:110px;width:786px;text-align:center;font-size:13px;line-height:18.8px}

  .card{position:absolute;top:196px;width:140px;height:140px;background:var(--white);
    display:flex;flex-direction:column;align-items:center;justify-content:flex-start;padding-top:28px}
  .card svg{width:64px;height:58px;fill:#2b2b2b}
  .card-label{margin-top:8px;font-size:12px;font-weight:500;color:var(--muted);text-align:center;line-height:14.5px;letter-spacing:.3px}
  .card.featured{top:192px;box-shadow:0 2px 6px rgba(0,0,0,.22)}
  .card.featured .card-label{color:var(--heading)}

  .partners{position:absolute;left:172px;top:1040px;width:800px;display:flex;justify-content:space-between;align-items:center}
  .partners span{font-size:18px;font-weight:600;color:var(--logo-grey)}

  .footer-rule{position:absolute;left:0;top:1110px;width:1200px;height:1px;background:var(--rule)}
  .footer-links{position:absolute;left:128px;top:1143px;font-size:11.6px;color:var(--text)}
  .footer-links a{color:var(--text);text-decoration:none}
  .footer-links .sep{margin:0 6px}
  .copyright{position:absolute;right:131px;top:1143px;font-size:11.6px;color:var(--text)}
</style>
</head>
<body>
  <header>
    <div class="brand">
      <div class="brand-mark"></div>
      <div>
        <div class="brand-name">Brisk Holloway</div>
        <div class="brand-tag">aviation security consulting</div>
      </div>
    </div>
    <nav class="main-nav">
      <a href="#">WHO WE ARE</a>
      <a href="#">WHAT WE DO</a>
      <a href="#">WHERE WE WORK</a>
      <a href="#">PROJECTS</a>
      <a href="#">LEADERSHIP</a>
      <a href="#">CONTACT</a>
    </nav>
  </header>

  <section class="hero">
    <div class="hero-band" role="img" aria-label="Blue-tinted airport apron panorama"></div>
    <h1 class="hero-title">Welcome to Brisk Holloway<br>aviation security consulting</h1>
    <div class="hero-frame">
      <div class="hero-photo" role="img" aria-label="Passenger jet parked at an airport gate with a pushback tug"></div>
    </div>
    <div class="slider-dots"><span class="active"></span><span></span><span></span><span></span></div>
    <div class="hero-copy">
      <p>Brisk Holloway works with government and industry on aviation security regulatory and operational strategy, governance, and oversight.Lorem ipsum dolor sit amet, consectetur adipiscing elit, sed do eiusmod tempor incididunt ut labo</p>
      <p>Lorem ipsum dolor sit amet, consectetur adipiscing elit, sed do eiusmod tempor incididunt ut labore et dolore magna aliqua. Ut enim ad minim veniam, quis nostrud exercitation.</p>
    </div>
    <a class="btn-read" href="#">READ MORE</a>
  </section>

  <section class="practice">
    <h2>Practice Areas</h2>
    <div class="underline"></div>
    <p class="intro">Lorem ipsum dolor sit amet, consectetur adipiscing elit, sed do eiusmod tempor incididunt ut labore et dolore magna aliqua. Ut enim ad minim veniam, quis nostrud exercitation ullamco laboris nisi ut aliquip ex ea commodo consequat. Duis aute irure dolor in reprehenderit in voluptate velit esse cillum dolore eu fugiat nulla pariatur.</p>

    <div class="card featured" style="left:178px">
      <svg viewBox="0 0 64 58" aria-hidden="true">
        <path d="M22 10a14 14 0 0 1 20 0l-2 2a11 11 0 0 0-16 0z"/>
        <path d="M26 15a8 8 0 0 1 12 0l-2 2a5 5 0 0 0-8 0z"/>
        <circle cx="32" cy="21" r="2.5"/>
        <path d="M29 26h6l2 10 24 6v3l-24-2-2 8h-6l-2-8-24 2v-3l24-6z"/>
      </svg>
      <div class="card-label">REGULATORS</div>
    </div>

    <div class="card" style="left:341px">
      <svg viewBox="0 0 64 58" aria-hidden="true">
        <path d="M14 14l6-2 8 6 18-8c4-2 8-1 8 1s-3 4-7 6l-18 8-4 10-4 1 1-9-9 3-4-3 4-3z"/>
        <path d="M6 40h10l12 4c3 1 3 4 0 4H18v2h12l16-8c3-1 5 2 2 4L32 56H6z"/>
      </svg>
      <div class="card-label">CAPACITY<br>DEVELOPMENT</div>
    </div>

    <div class="card" style="left:504px">
      <svg viewBox="0 0 64 58" aria-hidden="true">
        <path d="M4 20h18v5H4z"/><path d="M7 25h12v4H7z"/><path d="M11 29h4v20h-4z"/>
        <path d="M15 38h45v3H15zM20 41h3v8h-3zM30 41h3v8h-3zM40 41h3v8h-3zM50 41h3v8h-3zM57 38h3v11h-3z"/>
        <path d="M4 49h56v3H4z"/>
        <path d="M38 12l14-5c3-1 5 0 4 1l-14 6-3 6h-2l1-5-6 2-2-1z"/>
      </svg>
      <div class="card-label">AIRPORTS</div>
    </div>

    <div class="card" style="left:667px">
      <svg viewBox="0 0 64 58" aria-hidden="true">
        <circle cx="14" cy="10" r="8" fill="none" stroke="#2b2b2b" stroke-width="2"/>
        <path d="M13 5h2v5h4v2h-6z"/>
        <path d="M46 14l6 2-8 30H28l4-14h10z"/>
        <path d="M30 30l8-10 6 4-8 10z"/>
        <path d="M4 38h20v3H4zM12 41h3v11h-3z"/>
        <path d="M18 34h3v4h-3z"/>
      </svg>
      <div class="card-label">AIRLINES</div>
    </div>

    <div class="card" style="left:830px">
      <svg viewBox="0 0 64 58" aria-hidden="true">
        <path d="M10 4h8l12 38h22v3H28L16 7h-6z"/>
        <circle cx="26" cy="49" r="5"/>
        <path d="M24 16h18v12H28z" fill="none" stroke="#2b2b2b" stroke-width="3"/>
        <path d="M30 28h20v12H33z" fill="none" stroke="#2b2b2b" stroke-width="3"/>
      </svg>
      <div class="card-label">AIR CARGO</div>
    </div>
  </section>

  <div class="partners">
    <span>Harbor Atlantic</span>
    <span>Unitas</span>
    <span>Kestrel Airlines</span>
    <span>Tarvo</span>
    <span>Alpenjet</span>
    <span>Lumen Airways</span>
  </div>

  <footer>
    <div class="footer-rule"></div>
    <div class="footer-links"><a href="#">Home</a><span class="sep">|</span><a href="#">About</a><span class="sep">|</span><a href="#">Contact Us</a></div>
    <div class="copyright">© 2016 Brisk Holloway. All Rights Reserved.</div>
  </footer>
</body>
</html>
```